Webbanner-Design für Affiliate Marketing
Zielgruppe
Online-Shop für Kopfbedeckungen aller Art (Hüte, Mützen, Fascinator, Stirnbänder)
Design soll eine möglichst große Zielgruppe ansprechen (Hauptfokus: 18-34 Jahre). Also alle Online-Shopper mit einer Vorliebe für Hüte/ Mützen.
Aufgabenstellung
Insgesamt ein modernes, eingängiges und stilvolles Design. Nicht allzu verspielt oder zu unruhig. Fokus auf das Wesentliche.
Text: A Headwear for Everyone
B Hüte und Mützen, Top Auswahl, Kostenlose Lieferung
C Gut behütet durch den Winter
D Der Hut-Online-Shop
Das Lumo Vanta Logo soll mit eingebunden werden. Keine vorgegebene Platzierung, sprich dem Design anpassen.
Formate: (Breite x Höhe)
1. Full Banner - 468 x 60 Pixel, max. 40k Dateigröße
2. Medium Rectangle - 300 x 250 Pixel, max. 40k Dateigröße
3. Vertical Banner - 120 x 240 Pixel, max. 30k Dateigröße
4. Rectangle - 180 x 150 Pixel, max. 40k Dateigröße

```html
<!DOCTYPE html>
<html lang="de">
<head>
<meta charset="utf-8">
<title>Lumo Vanta – Rectangle Banner</title>
<link rel="stylesheet" href="https://fonts.googleapis.com/css2?family=Oswald:wght@400;500;600&display=swap">
<style>
  :root {
    --page-bg: #eceae8;
    --banner-white: #ffffff;
    --brand-red: #ef4b45;
    --ink-dark: #2a2a2a;
    --text-light: #ffffff;
    --photo-deep: #1f1a18;
    --photo-mid: #4a362e;
    --photo-warm: #9a7464;
  }
  * { margin: 0; padding: 0; box-sizing: border-box; }
  html, body {
    width: 1200px; height: 800px; overflow: hidden;
    background: var(--page-bg);
    font-family: "Oswald", "Arial Narrow", sans-serif;
  }
  .banner {
    position: absolute; left: 150px; top: 25px;
    width: 900px; height: 750px;
    background: var(--banner-white);
    overflow: hidden;
  }
  .banner-photo { position: absolute; inset: 0; }
  .brand {
    position: absolute; left: 40px; top: 38px;
    display: flex; align-items: center; gap: 18px;
    color: var(--ink-dark);
    font-weight: 500; font-size: 54px; line-height: 1;
    letter-spacing: 2px; text-transform: uppercase;
  }
  .brand-dot {
    width: 44px; height: 44px; border-radius: 50%;
    background: var(--brand-red);
  }
  .tagline-band {
    position: absolute; left: 0; top: 140px;
    width: 600px; height: 62px;
    background: var(--brand-red);
    color: var(--text-light);
    font-size: 42px; font-weight: 400; line-height: 62px;
    padding-left: 28px; letter-spacing: 1px;
  }
  .headline {
    position: absolute; left: 22px; top: 222px;
    color: var(--text-light);
    text-transform: uppercase;
    font-weight: 600; font-size: 82px; line-height: 1;
  }
  .subline {
    position: absolute; left: 22px; top: 312px;
    color: var(--text-light);
    font-weight: 400; font-size: 40px; line-height: 1;
  }
  .benefits {
    position: absolute; left: 22px; top: 540px;
    list-style: none;
    color: var(--text-light);
    font-weight: 500; font-size: 40px; line-height: 46px;
  }
  .benefits li { display: flex; align-items: center; gap: 18px; }
  .benefits svg { width: 18px; height: 22px; flex: none; }
  .shop-button {
    position: absolute; left: 530px; top: 632px;
    width: 350px; height: 84px;
    background: var(--brand-red);
    color: var(--text-light);
    font-weight: 500; font-size: 52px; line-height: 84px;
    text-align: center; text-transform: uppercase;
    text-decoration: none;
  }
</style>
</head>
<body>
  <div class="banner">
    <svg class="banner-photo" viewBox="0 0 900 750" role="img" aria-label="Photo of two young women wearing hats, one in a dark fedora with patterned band in the foreground">
      <defs>
        <linearGradient id="photo-tone" x1="0" y1="0" x2="1" y2="0.3">
          <stop offset="0" stop-color="var(--photo-deep)"/>
          <stop offset="0.35" stop-color="var(--photo-mid)"/>
          <stop offset="0.7" stop-color="var(--photo-warm)"/>
          <stop offset="1" stop-color="var(--photo-mid)"/>
        </linearGradient>
      </defs>
      <path d="M0 140 H470 Q520 20 620 10 H900 V750 H0 Z" fill="url(#photo-tone)"/>
    </svg>

    <div class="brand"><span class="brand-dot"></span>Lumo Vanta</div>
    <div class="tagline-band">Der Hut-Online-Shop</div>

    <h1 class="headline">Headwear</h1>
    <p class="subline">for Everyone</p>

    <ul class="benefits">
      <li><svg viewBox="0 0 18 22"><path d="M2 2 L16 11 L2 20 Z" fill="#fff"/></svg>Hüte und Mützen</li>
      <li><svg viewBox="0 0 18 22"><path d="M2 2 L16 11 L2 20 Z" fill="#fff"/></svg>Top Auswahl</li>
      <li><svg viewBox="0 0 18 22"><path d="M2 2 L16 11 L2 20 Z" fill="#fff"/></svg>Kostenlose Lieferung</li>
    </ul>

    <a class="shop-button" href="#">Zum Shop</a>
  </div>
</body>
</html>
```